Printing company needs website!

A printing company would like a new professional website (made with wix). Now they don't have a website, but they want a unique, beautiful, clear site. Of course they provide the content themselves, we are now looking for the beautiful design with some mockups. You can see several of their projects on their instagram & facebook.
Www.pagenook.com/velmoor and https://www.snapfolio.com/velmoor.be/ logos are attached.

```html
<!DOCTYPE html>
<html lang="en">
<head>
<meta charset="utf-8">
<title>Velmoor – The Best Printing Solutions</title>
<link href="https://fonts.googleapis.com/css2?family=Alegreya+Sans:ital,wght@0,300;0,400;0,500;0,700;0,800;1,400&family=Alegreya:wght@400;700&display=swap" rel="stylesheet">
<style>
:root{
  --blue:#1aa3d9;
  --teal:#45c1b0;
  --yellow:#f7cd1c;
  --dark:#231f20;
  --ink:#1c1c1c;
  --grey:#555;
  --pale:#eef8fb;
  --card:#eaf6f9;
  --white:#fff;
}
*{box-sizing:border-box;margin:0;padding:0}
html,body{width:1200px;height:4967px;overflow:hidden}
body{position:relative;background:var(--white);font-family:"Alegreya Sans",sans-serif;color:var(--ink)}
.abs{position:absolute}
.serif{font-family:"Alegreya",serif}

/* header */
.brand{left:68px;top:14px;display:flex;align-items:center;gap:12px}
.brand-dot{width:64px;height:64px;border-radius:50%;background:var(--teal)}
.brand-name{font-size:50px;font-weight:700;color:#333;line-height:1}
.brand-tag{left:218px;top:70px;font-size:15px;color:var(--teal)}
.topbar{left:637px;top:0;height:39px;display:flex;font-size:15px;color:var(--white)}
.topbar div{display:flex;align-items:center;justify-content:center;gap:8px;height:39px}
.tb-phone{width:168px;background:var(--teal)}
.tb-search{width:110px;background:var(--yellow)}
.tb-sign{width:113px;background:var(--teal);font-weight:700}
.nav{top:72px;left:0;width:1200px;font-size:17px;color:#333}
.nav span{position:absolute}
.nav .active{color:var(--blue);border-bottom:2px solid var(--blue);padding-bottom:4px}

/* hero */
.hero{left:0;top:106px}
.hero-title{left:0;width:1200px;top:365px;text-align:center;font-size:118px;font-weight:700;color:var(--white);line-height:1}
.hero-sub{left:0;width:1200px;top:500px;text-align:center;font-size:50px;font-weight:400;color:var(--white)}

/* about */
.about-h{left:172px;top:832px;font-size:56px;font-weight:700}
.about-h b{color:var(--blue)}
.about-sub{left:172px;top:906px;font-size:45px;font-weight:300;color:var(--teal)}
.about-line{left:172px;top:964px;width:393px;height:3px;background:var(--teal)}
.about-mark{left:176px;top:1012px;width:400px;height:395px;border-radius:50%;background:radial-gradient(circle at 40% 40%,#cfeff0,#e9f7fa);display:flex;align-items:center;justify-content:center;font-size:64px;font-weight:700;color:var(--teal)}
.about-copy{left:633px;top:848px;width:412px;font-size:17px;line-height:1.33;color:#333}
.feature{width:200px}
.feature svg{position:absolute;left:0;top:0}
.feature h4{position:absolute;left:54px;top:-8px;font-size:24px;font-weight:500;color:var(--yellow);white-space:nowrap}
.feature p{position:absolute;left:54px;top:22px;width:140px;font-size:12.5px;line-height:1.45;color:#333}

/* section titles */
.sec-bg{left:0;width:1200px;background:var(--pale)}
.sec-title{left:0;width:1200px;text-align:center;font-size:58px;font-weight:700;color:var(--ink)}
.btn{width:156px;height:46px;border-radius:23px;background:var(--teal);color:var(--white);font-size:20px;font-weight:500;display:flex;align-items:center;justify-content:center;left:522px}

/* works */
.work{width:267px;height:255px}
.w1{background:linear-gradient(135deg,#5aa9d8,#7bbde0)}
.w2{background:linear-gradient(135deg,#f5cf2b,#f3c21b)}
.w3{background:linear-gradient(135deg,#5ec9b9,#49b8a8);border-bottom-right-radius:40px}
.w4{background:linear-gradient(160deg,#ffffff 0%,#dff1f8 40%,#f2c41f 100%)}
.w5{background:linear-gradient(135deg,#f5cf2b,#e8b617);border-bottom-right-radius:40px}
.w6{background:linear-gradient(135deg,#3b3b3b,#707070);border-bottom-right-radius:40px}

/* services */
.svc{width:270px;height:238px;background:var(--card);border-radius:50px 20px 50px 20px;text-align:center}
.svc svg{position:absolute;left:50%;transform:translateX(-50%);top:34px}
.svc h4{position:absolute;left:0;width:100%;top:118px;font-size:20px;font-weight:500;color:var(--yellow)}
.svc p{position:absolute;left:30px;width:210px;top:146px;font-size:14px;line-height:1.6;color:#444}

/* news */
.news{left:172px;width:414px;height:122px;background:var(--white);border:2px solid #ccc;display:flex}
.news-date{width:90px;height:100%;color:var(--white);display:flex;flex-direction:column;align-items:center;justify-content:center;font-size:29px;font-weight:500;line-height:1.15}
.news-date b{font-size:34px;font-weight:700}
.news-text{padding:18px 0 0 22px;font-size:21px;font-weight:700;line-height:1.35;color:var(--ink)}
.news-photo{left:600px;top:3406px;width:426px;height:444px;border:2px solid #ccc;background:linear-gradient(180deg,#3b3f44 0%,#6b7077 35%,#e7c9a1 55%,#7fb3c9 70%,#2f3236 100%)}

/* testimonials */
.tcard{width:268px;height:282px;border-radius:40px 60px 40px 40px;color:var(--white);text-align:center}
.tq{position:absolute;left:0;width:100%;top:52px;font-family:"Alegreya",serif;font-size:96px;font-weight:700;line-height:1}
.tcard p{position:absolute;left:18px;width:232px;top:140px;font-size:16px;font-style:italic;line-height:1.4}
.tcard h5{position:absolute;left:0;width:100%;top:242px;font-size:21px;font-weight:400}
.avatar{width:92px;height:92px;border-radius:50%;border:4px solid var(--white);background:linear-gradient(180deg,#b9bfc6,#5d646c)}
.arrow{width:62px;height:62px;border-radius:50%;background:#ececec;display:flex;align-items:center;justify-content:center}

/* footer */
.footer{left:0;top:4533px;width:1200px;height:434px;background:var(--dark)}
.f-brand{left:154px;top:4586px;display:flex;align-items:center;gap:10px}
.f-brand .brand-dot{width:52px;height:52px}
.f-brand .brand-name{font-size:42px;color:var(--white)}
.f-tag{left:266px;top:4626px;font-size:13px;color:var(--teal)}
.f-about{left:172px;top:4668px;width:260px;font-size:13px;line-height:1.5;color:var(--white)}
.social{width:40px;height:40px;border-radius:50%}
.f-h{font-size:34px;font-weight:700;color:var(--white)}
.f-list{font-size:20px;line-height:36px;color:var(--white)}
.f-rule{left:0;top:4880px;width:1200px;height:1px;background:#555}
.copy{left:0;width:1200px;top:4908px;text-align:center;font-size:15px;color:var(--white)}
</style>
</head>
<body>

<!-- header -->
<div class="abs brand"><span class="brand-dot"></span><span class="brand-name">Velmoor</span></div>
<div class="abs brand-tag">waar alles velmoor is</div>

<div class="abs topbar">
  <div class="tb-phone">
    <svg width="18" height="18" viewBox="0 0 24 24"><path d="M6.6 10.8a15.1 15.1 0 0 0 6.6 6.6l2.2-2.2c.3-.3.7-.4 1-.2 1.1.4 2.3.6 3.6.6.6 0 1 .4 1 1V20c0 .6-.4 1-1 1A17 17 0 0 1 3 4c0-.6.4-1 1-1h3.5c.6 0 1 .4 1 1 0 1.3.2 2.5.6 3.6.1.3 0 .7-.2 1z" fill="#fff"/></svg>
    +1 555 014 2270
  </div>
  <div class="tb-search">
    <svg width="18" height="18" viewBox="0 0 24 24"><circle cx="10" cy="10" r="6" fill="none" stroke="#fff" stroke-width="2.5"/><line x1="14.5" y1="14.5" x2="20" y2="20" stroke="#fff" stroke-width="2.5"/></svg>
    Search
  </div>
  <div class="tb-sign">SIGN UP</div>
</div>

<div class="abs nav">
  <span class="active" style="left:449px">Home</span>
  <span style="left:526px">About Us</span>
  <span style="left:626px">Services</span>
  <span style="left:725px">Testimonial</span>
  <span style="left:848px">Projects</span>
  <span style="left:938px">Contact Us</span>
</div>

<!-- hero -->
<svg class="abs hero" width="1200" height="650" viewBox="0 0 1200 650" role="img" aria-label="Photo of a print shop worker operating a large-format printer">
  <defs>
    <linearGradient id="heroPhoto" x1="0" y1="0" x2="1" y2="1">
      <stop offset="0" stop-color="#8a8d91"/>
      <stop offset="0.45" stop-color="#5a5d62"/>
      <stop offset="1" stop-color="#3c3d40"/>
    </linearGradient>
  </defs>
  <path d="M0 0H1200V470C1185 565 1115 598 1010 598H0Z" fill="url(#heroPhoto)"/>
  <path d="M0 612H1010C1125 612 1192 570 1200 500" fill="none" stroke="#f7cd1c" stroke-width="11"/>
  <path d="M0 626H1010C1135 626 1200 585 1212 505" fill="none" stroke="#45c1b0" stroke-width="11"/>
  <path d="M0 640H1010C1145 640 1210 598 1224 510" fill="none" stroke="#1aa3d9" stroke-width="11"/>
</svg>
<div class="abs hero-title">Velmoor</div>
<div class="abs hero-sub">The Best Printing Solutions</div>

<!-- about -->
<h2 class="abs about-h">About <b>Velmoor</b></h2>
<div class="abs about-sub">Waar Alles Velmoor is</div>
<div class="abs about-line"></div>
<div class="abs about-mark"><span style="width:110px;height:110px;border-radius:50%;background:var(--teal);display:block"></span></div>
<p class="abs about-copy serif">Lorem ipsum dolor sit amet, consectetur adipiscing elit, sed do eiusmod tempor incididunt ut labore et dolore magna aliqua. Ut enim ad minim veniam, quis nostrud exercitation ullamco laboris nisi ut aliquip ex ea commodo consequat.</p>

<div class="abs feature" style="left:633px;top:1010px">
  <svg width="42" height="42" viewBox="0 0 42 42"><path d="M36 4C24 6 16 14 12 24l6 6c10-4 18-12 20-24z" fill="#1aa3d9"/><circle cx="27" cy="15" r="3.5" fill="#fff"/><path d="M12 24l-7 1 5-8zM18 30l-1 7 8-5z" fill="#1aa3d9"/><path d="M10 30l-5 7 7-5z" fill="#45c1b0"/></svg>
  <h4>Speed</h4><p class="serif">Lorem ipsum dolor sit amet, consectetur dolore magna aliqua.</p>
</div>
<div class="abs feature" style="left:849px;top:1010px">
  <svg width="42" height="42" viewBox="0 0 42 42"><circle cx="21" cy="16" r="12" fill="none" stroke="#1aa3d9" stroke-width="3"/><path d="M15 16l4 4 8-8" fill="none" stroke="#45c1b0" stroke-width="3"/><path d="M13 26l-4 12 6-3 3 5 3-10M29 26l4 12-6-3-3 5-3-10" fill="#1aa3d9"/></svg>
  <h4>Quality</h4><p class="serif">Lorem ipsum dolor sit amet, consectetur dolore magna aliqua.</p>
</div>
<div class="abs feature" style="left:633px;top:1152px">
  <svg width="42" height="42" viewBox="0 0 42 42"><circle cx="22" cy="12" r="9" fill="#1aa3d9"/><text x="22" y="17" font-size="13" text-anchor="middle" fill="#fff" font-family="sans-serif" font-weight="700">$</text><path d="M2 30h8l8 2h8l10-6 2 3-12 9H8v-8" fill="#45c1b0"/></svg>
  <h4>Lowprice</h4><p class="serif">Lorem ipsum dolor sit amet, consectetur dolore magna aliqua.</p>
</div>
<div class="abs feature" style="left:849px;top:1152px">
  <svg width="44" height="42" viewBox="0 0 44 42"><rect x="14" y="4" width="26" height="34" rx="3" fill="#1aa3d9"/><rect x="18" y="9" width="18" height="6" fill="#fff"/><circle cx="12" cy="24" r="9" fill="#45c1b0"/><text x="12" y="29" font-size="12" text-anchor="middle" fill="#fff" font-family="sans-serif" font-weight="700">$</text></svg>
  <h4>Easy Payment</h4><p class="serif">Lorem ipsum dolor sit amet, consectetur dolore magna aliqua.</p>
</div>
<div class="abs feature" style="left:633px;top:1295px">
  <svg width="42" height="42" viewBox="0 0 42 42"><circle cx="19" cy="20" r="15" fill="none" stroke="#1aa3d9" stroke-width="3"/><path d="M19 11v9h7" fill="none" stroke="#1aa3d9" stroke-width="3"/><circle cx="31" cy="31" r="8" fill="#45c1b0"/><path d="M27 31l3 3 5-5" fill="none" stroke="#fff" stroke-width="2.5"/></svg>
  <h4>Quick Service</h4><p class="serif">Lorem ipsum dolor sit amet, consectetur dolore magna aliqua.</p>
</div>
<div class="abs feature" style="left:849px;top:1295px">
  <svg width="42" height="42" viewBox="0 0 42 42"><rect x="3" y="6" width="36" height="24" rx="2" fill="#1aa3d9"/><rect x="6" y="9" width="30" height="18" fill="#45c1b0"/><rect x="17" y="30" width="8" height="6" fill="#1aa3d9"/><rect x="11" y="36" width="20" height="3" fill="#1aa3d9"/></svg>
  <h4>All In One</h4><p class="serif">Lorem ipsum dolor sit amet, consectetur dolore magna aliqua.</p>
</div>

<!-- works -->
<div class="abs sec-bg" style="top:1560px;height:862px"></div>
<h2 class="abs sec-title" style="top:1600px">Our Works</h2>
<div class="abs work w1" style="left:173px;top:1713px" role="img" aria-label="Social post promoting custom printed coasters"></div>
<div class="abs work w2" style="left:465px;top:1713px" role="img" aria-label="Yellow birthday poster design"></div>
<div class="abs work w3" style="left:756px;top:1713px" role="img" aria-label="Promotional post for printed flags"></div>
<div class="abs work w4" style="left:173px;top:2015px" role="img" aria-label="Post about a printed delivery van wrap"></div>
<div class="abs work w5" style="left:465px;top:2015px" role="img" aria-label="Post about printed stickers and product labels"></div>
<div class="abs work w6" style="left:756px;top:2015px" role="img" aria-label="Post about personalised notepads"></div>
<div class="abs btn" style="top:2321px">VIEW MORE</div>

<!-- services -->
<h2 class="abs sec-title" style="top:2475px">Our Services</h2>

<div class="abs svc" style="left:172px;top:2579px">
  <svg width="80" height="62" viewBox="0 0 80 62"><rect x="6" y="4" width="44" height="30" rx="4" fill="#1aa3d9" transform="rotate(-14 28 19)"/><rect x="12" y="16" width="60" height="40" rx="5" fill="#1aa3d9"/><circle cx="26" cy="34" r="5" fill="#fff"/><rect x="38" y="30" width="26" height="4" fill="#fff"/><rect x="38" y="39" width="18" height="4" fill="#fff"/></svg>
  <h4>Business Card</h4><p class="serif">Lorem ipsum dolor sit amet, adipiscing elit, sed do eiusmod tempor ialiqua.</p>
</div>
<div class="abs svc" style="left:465px;top:2579px">
  <svg width="60" height="66" viewBox="0 0 60 66"><rect x="8" y="6" width="44" height="56" fill="#f7cd1c"/><path d="M30 6l8-6v10z" fill="#f7cd1c"/><path d="M30 42l-9-9a5 5 0 0 1 9-5 5 5 0 0 1 9 5z" fill="none" stroke="#fff" stroke-width="3"/></svg>
  <h4>Post Card</h4><p class="serif">Lorem ipsum dolor sit amet, adipiscing elit, sed do eiusmod tempor ialiqua.</p>
</div>
<div class="abs svc" style="left:757px;top:2579px">
  <svg width="72" height="72" viewBox="0 0 72 72"><polygon points="36,2 44,9 54,6 57,16 67,20 64,30 70,38 63,45 64,56 53,57 47,66 37,62 27,68 21,59 10,57 10,46 3,38 9,30 6,20 16,16 20,6 30,9" fill="#45c1b0"/><text x="36" y="42" text-anchor="middle" font-size="16" font-weight="700" fill="#fff" font-family="sans-serif">SALE</text></svg>
  <h4>Stickers &amp; Label</h4><p class="serif">Lorem ipsum dolor sit amet, adipiscing elit, sed do eiusmod tempor ialiqua.</p>
</div>
<div class="abs svc" style="left:172px;top:2870px">
  <svg width="56" height="72" viewBox="0 0 56 72"><rect x="6" y="4" width="44" height="58" fill="#1aa3d9"/><text x="28" y="22" text-anchor="middle" font-size="15" font-weight="700" fill="#fff" font-family="sans-serif">ADS</text><rect x="12" y="30" width="32" height="3" fill="#fff"/><rect x="12" y="38" width="32" height="3" fill="#fff"/><rect x="12" y="46" width="22" height="3" fill="#fff"/><path d="M40 62l10 8V54z" fill="#1aa3d9"/></svg>
  <h4>Flyers</h4><p class="serif">Lorem ipsum dolor sit amet, adipiscing elit, sed do eiusmod tempor ialiqua.</p>
</div>
<div class="abs svc" style="left:465px;top:2870px">
  <svg width="80" height="60" viewBox="0 0 80 60"><rect x="2" y="6" width="76" height="50" rx="4" fill="#f7cd1c"/><path d="M4 10l36 26 36-26" fill="none" stroke="#fff" stroke-width="4"/></svg>
  <h4>Envelope</h4><p class="serif">Lorem ipsum dolor sit amet, adipiscing elit, sed do eiusmod tempor ialiqua.</p>
</div>
<div class="abs svc" style="left:757px;top:2870px">
  <svg width="60" height="72" viewBox="0 0 60 72"><rect x="8" y="8" width="44" height="60" fill="#45c1b0"/><path d="M20 8l6-8 4 8z" fill="#45c1b0"/><path d="M18 30l12 8 12-8v16l-12-8-12 8z" fill="none" stroke="#fff" stroke-width="3"/><line x1="30" y1="20" x2="30" y2="58" stroke="#fff" stroke-width="3"/></svg>
  <h4>Gifting Card</h4><p class="serif">Lorem ipsum dolor sit amet, adipiscing elit, sed do eiusmod tempor ialiqua.</p>
</div>
<div class="abs btn" style="top:3150px">VIEW MORE</div>

<!-- news -->
<div class="abs sec-bg" style="top:3258px;height:676px"></div>
<h2 class="abs sec-title" style="top:3296px">Latest News</h2>
<div class="abs news" style="top:3406px"><div class="news-date" style="background:var(--blue)">JAN<b>25</b></div><div class="news-text serif">Lorem ipsum dolor sit<br>amet,&nbsp; adipiscing elit, sed do<br>vel facilisis.</div></div>
<div class="abs news" style="top:3567px"><div class="news-date" style="background:var(--yellow)">FEB<b>03</b></div><div class="news-text serif">Lorem ipsum dolor sit<br>amet,&nbsp; adipiscing elit, sed do<br>vel facilisis.</div></div>
<div class="abs news" style="top:3727px"><div class="news-date" style="background:var(--teal)">JAN<b>31</b></div><div class="news-text serif">Lorem ipsum dolor sit<br>amet,&nbsp; adipiscing elit, sed do<br>vel facilisis.</div></div>
<div class="abs news-photo" role="img" aria-label="Photo of colourful printed sheets running through an offset press"></div>

<!-- testimonials -->
<h2 class="abs sec-title" style="top:4000px">Testimonials</h2>
<div class="abs tcard" style="left:172px;top:4147px;background:var(--blue)"><div class="tq">&ldquo;</div><p>Lorem ipsum dolor sit amet, consectetur adipiscing elit, sed do eiusmod tempor incididunt ut labore et dolore magna aliqua.</p><h5>MAREN TOLLE</h5></div>
<div class="abs tcard" style="left:466px;top:4147px;background:var(--yellow)"><div class="tq">&ldquo;</div><p>Lorem ipsum dolor sit amet, consectetur adipiscing elit, sed do eiusmod tempor incididunt ut labore et dolore magna aliqua.</p><h5>OSKAR VENNEL</h5></div>
<div class="abs tcard" style="left:761px;top:4147px;background:var(--teal)"><div class="tq">&ldquo;</div><p>Lorem ipsum dolor sit amet, consectetur adipiscing elit, sed do eiusmod tempor incididunt ut labore et dolore magna aliqua.</p><h5>LIDIA ROSE</h5></div>
<div class="abs avatar" style="left:260px;top:4098px" role="img" aria-label="Portrait of client Maren Tolle"></div>
<div class="abs avatar" style="left:554px;top:4098px" role="img" aria-label="Portrait of client Oskar Vennel"></div>
<div class="abs avatar" style="left:849px;top:4098px" role="img" aria-label="Portrait of client Lidia Rose"></div>
<div class="abs arrow" style="left:59px;top:4260px"><svg width="26" height="22" viewBox="0 0 26 22"><path d="M24 11H4M12 2L3 11l9 9" fill="none" stroke="#fff" stroke-width="3.5"/></svg></div>
<div class="abs arrow" style="left:1078px;top:4260px"><svg width="26" height="22" viewBox="0 0 26 22"><path d="M2 11h20M14 2l9 9-9 9" fill="none" stroke="#fff" stroke-width="3.5"/></svg></div>

<!-- footer -->
<div class="abs footer"></div>
<svg class="abs" style="left:0;top:4490px" width="1200" height="90" viewBox="0 0 1200 90">
  <path d="M0 90C0 50 40 42 150 42H1200V90Z" fill="#231f20"/>
  <path d="M-2 80C0 25 45 8 150 8H1200" fill="none" stroke="#1aa3d9" stroke-width="11"/>
  <path d="M-2 88C2 38 50 21 150 21H1200" fill="none" stroke="#45c1b0" stroke-width="11"/>
  <path d="M-2 96C4 50 55 34 150 34H1200" fill="none" stroke="#f7cd1c" stroke-width="11"/>
</svg>

<div class="abs f-brand"><span class="brand-dot"></span><span class="brand-name">Velmoor</span></div>
<div class="abs f-tag">waar alles velmoor is</div>
<p class="abs f-about serif">Lorem ipsum dolor sit amet, consectetur adipiscing elit, sed do eiusmod tempor incididunt ut labore et dolore magna aliqua.</p>
<div class="abs social" style="left:174px;top:4748px;background:var(--blue)"></div>
<div class="abs social" style="left:234px;top:4748px;background:var(--yellow)"></div>
<div class="abs social" style="left:294px;top:4748px;background:var(--teal)"></div>

<div class="abs f-h" style="left:467px;top:4575px">Links</div>
<div class="abs f-list serif" style="left:469px;top:4630px">Home<br>About Us<br>Services<br>Testimonials<br>Projects<br>Contact Us</div>

<div class="abs f-h" style="left:650px;top:4575px">Contact Us</div>
<svg class="abs" style="left:652px;top:4638px" width="30" height="30" viewBox="0 0 30 30"><rect width="30" height="30" fill="#1aa3d9"/><path d="M15 5a7 7 0 0 0-7 7c0 5 7 13 7 13s7-8 7-13a7 7 0 0 0-7-7z" fill="#fff"/><circle cx="15" cy="12" r="2.5" fill="#1aa3d9"/></svg>
<div class="abs f-list serif" style="left:699px;top:4632px;line-height:26px">123 ipsum dolor<br>amet, dolore<br>magna aliqua.</div>
<svg class="abs" style="left:652px;top:4720px" width="30" height="30" viewBox="0 0 30 30"><rect width="30" height="30" fill="#f7cd1c"/><path d="M10 8h4l1 5-2 1a9 9 0 0 0 4 4l1-2 5 1v4c-9 0-15-6-15-13z" fill="#fff"/></svg>
<div class="abs f-list serif" style="left:699px;top:4717px">+1 555 014 2270</div>
<svg class="abs" style="left:652px;top:4770px" width="30" height="30" viewBox="0 0 30 30"><rect width="30" height="30" fill="#45c1b0"/><rect x="6" y="9" width="18" height="12" fill="#fff"/><path d="M6 9l9 7 9-7" fill="none" stroke="#45c1b0" stroke-width="2"/></svg>
<div class="abs f-list serif" style="left:699px;top:4767px">Info@Velmoor.com</div>

<div class="abs f-h" style="left:922px;top:4575px">Policies</div>
<div class="abs f-list serif" style="left:922px;top:4630px;line-height:26px">Privacy<br><span style="display:block;margin-top:10px">Terms &amp;<br>conditions</span><span style="display:block;margin-top:10px">Cookie</span></div>

<div class="abs f-rule"></div>
<div class="abs copy">Copyrights © 2022Velmoor I All Rights Reserved</div>

</body>
</html>
```